依頼詳細
比較する栄養素が多いので、どうすればお客様に見て頂きやすいか、
スマホで見た時に伝わりやすいかを重視したデザインにしていただきたいです。

添付している「参考画像」のようなグラフにしようと思ったのですが、
横長に作られており、スマホで見ると文字が小さくなって見づらいのではと思い
こちらでデザインを募らせていただく事となりました。

今のLPに差し込んでも違和感のないデザインでお願いします。

なお、今回はデザインのみでコーディングは必要ありません。
サイトURL
https://rinohaze.com/lp/
ページ数
1ページ
希望イメージ
シンプル 複雑
単色 カラフル
暗い 明るい
日常 高級
遊び心 厳粛
未来的 伝統的
女性的 男性的
希望する色
青系、無彩色系
納品ファイル
• 高解像度JPG (.jpg)
• イラストレーター形式 (.ai)
• フォトショップ形式 (.psd)
補足説明
■ 選んだ理由

一番バランスの良いデザインでした。

■ 提案者全員のお礼・コメント

この度は沢山のご提案ありがとうございました。
また機会がございましたら、どうぞよろしくお願いいたします。

```html
<!DOCTYPE html>
<html lang="ja">
<head>
<meta charset="UTF-8">
<title>栄養素比較グラフ</title>
<link rel="stylesheet" href="https://fonts.googleapis.com/css2?family=Noto+Sans+JP:wght@400;500;700&display=swap">
<style>
  :root {
    --ours: #f2935c;
    --retail: #cbdc9c;
    --mlm: #5a8fd6;
    --baseline: #27467a;
    --label-border: #c9d3e2;
    --ink: #333;
    --bg: #fff;
  }
  html, body { margin: 0; padding: 0; overflow: hidden; background: var(--bg); }
  .canvas { width: 851px; height: 1200px; position: relative; font-family: "Noto Sans JP", sans-serif; color: var(--ink); }
  svg { display: block; font-family: "Noto Sans JP", sans-serif; }
  .legend-text { font-size: 17px; font-weight: 500; fill: var(--ink); }
  .baseline-caption { font-size: 15px; font-weight: 500; fill: var(--baseline); }
  .baseline-value { font-size: 28px; font-weight: 700; fill: var(--baseline); }
  .baseline { stroke: var(--baseline); stroke-width: 3; }
  .label-box { fill: var(--bg); stroke: var(--label-border); stroke-width: 1.2; }
  .label-text { font-size: 15px; font-weight: 500; fill: var(--ink); }
  .value { font-size: 15px; font-weight: 500; fill: var(--ink); }
  .bar-ours { fill: var(--ours); }
  .bar-retail { fill: var(--retail); }
  .bar-mlm { fill: var(--mlm); }
  .break-gap { fill: none; stroke: var(--bg); stroke-width: 10; }
  .break-edge { fill: none; stroke: #999; stroke-width: 1.2; }
</style>
</head>
<body>
<div class="canvas">
<svg width="851" height="1200" viewBox="0 0 851 1200" role="img" aria-label="栄養素比較グラフ">
  <!-- legend -->
  <g class="legend">
    <rect class="bar-ours" x="40" y="12" width="16" height="16"/>
    <text class="legend-text" x="64" y="27">ニュートリベース</text>
    <rect class="bar-retail" x="330" y="12" width="16" height="16"/>
    <text class="legend-text" x="354" y="27">一般市販サプリ</text>
    <rect class="bar-mlm" x="580" y="12" width="16" height="16"/>
    <text class="legend-text" x="604" y="27">MLM系高級サプリ</text>
  </g>

  <!-- baseline -->
  <text class="baseline-caption" x="213" y="60" text-anchor="middle">基準値</text>
  <text class="baseline-value" x="213" y="92" text-anchor="middle">100%</text>
  <path d="M206,98 L213,106 L220,98 Z" fill="var(--baseline)"/>

  <!-- rows -->
  <g class="row" transform="translate(0,140)">
    <rect class="label-box" x="8" y="0" width="148" height="45"/><text class="label-text" x="16" y="28">ビタミンA</text>
    <rect class="bar-ours" x="156" y="9" width="14" height="8"/>
    <text class="value" x="224" y="17">100mcg</text>
  </g>
  <g class="row" transform="translate(0,189)">
    <rect class="label-box" x="8" y="0" width="148" height="45"/><text class="label-text" x="16" y="28">β-カロテン</text>
    <text class="value" x="224" y="17">2,000mcg</text>
  </g>
  <g class="row" transform="translate(0,238)">
    <rect class="label-box" x="8" y="0" width="148" height="45"/><text class="label-text" x="16" y="28">ビタミンC</text>
    <rect class="bar-ours" x="156" y="9" width="128" height="8"/>
    <rect class="bar-retail" x="156" y="19" width="80" height="8"/>
    <rect class="bar-mlm" x="156" y="29" width="42" height="8"/>
    <text class="value" x="296" y="17">200mg</text>
  </g>
  <g class="row" transform="translate(0,287)">
    <rect class="label-box" x="8" y="0" width="148" height="45"/><text class="label-text" x="16" y="28">ビタミンD3</text>
    <rect class="bar-ours" x="156" y="9" width="30" height="8"/>
    <rect class="bar-mlm" x="156" y="29" width="70" height="8"/>
    <text class="value" x="224" y="17">5.0mcg</text>
  </g>
  <g class="row" transform="translate(0,336)">
    <rect class="label-box" x="8" y="0" width="148" height="45"/><text class="label-text" x="16" y="28">ビタミンE</text>
    <rect class="bar-ours" x="156" y="9" width="626" height="8"/>
    <rect class="bar-retail" x="156" y="19" width="24" height="8"/>
    <rect class="bar-mlm" x="156" y="29" width="214" height="8"/>
    <text class="value" x="845" y="17" text-anchor="end">50.0mg</text>
  </g>
  <g class="row" transform="translate(0,385)">
    <rect class="label-box" x="8" y="0" width="148" height="45"/><text class="label-text" x="16" y="28">ビタミンB1</text>
    <rect class="bar-ours" x="156" y="9" width="626" height="8"/>
    <rect class="bar-retail" x="156" y="19" width="398" height="8"/>
    <rect class="bar-mlm" x="156" y="29" width="242" height="8"/>
    <text class="value" x="845" y="17" text-anchor="end">10.0mg</text>
  </g>
  <g class="row" transform="translate(0,434)">
    <rect class="label-box" x="8" y="0" width="148" height="45"/><text class="label-text" x="16" y="28">ビタミンB2</text>
    <rect class="bar-ours" x="156" y="9" width="370" height="8"/>
    <rect class="bar-retail" x="156" y="19" width="336" height="8"/>
    <rect class="bar-mlm" x="156" y="29" width="186" height="8"/>
    <text class="value" x="540" y="17">10.0mg</text>
  </g>
  <g class="row" transform="translate(0,483)">
    <rect class="label-box" x="8" y="0" width="148" height="45"/><text class="label-text" x="16" y="28">ナイアシン</text>
    <rect class="bar-ours" x="156" y="9" width="128" height="8"/>
    <rect class="bar-mlm" x="156" y="29" width="72" height="8"/>
    <text class="value" x="296" y="17">20mg</text>
  </g>
  <g class="row" transform="translate(0,532)">
    <rect class="label-box" x="8" y="0" width="148" height="45"/><text class="label-text" x="16" y="28">パントテン酸</text>
    <rect class="bar-ours" x="156" y="9" width="214" height="8"/>
    <rect class="bar-mlm" x="156" y="29" width="186" height="8"/>
    <text class="value" x="382" y="17">15.0mg</text>
  </g>
  <g class="row" transform="translate(0,581)">
    <rect class="label-box" x="8" y="0" width="148" height="45"/><text class="label-text" x="16" y="28">ビタミンB6</text>
    <rect class="bar-ours" x="156" y="9" width="626" height="8"/>
    <rect class="bar-retail" x="156" y="19" width="416" height="8"/>
    <rect class="bar-mlm" x="156" y="29" width="200" height="8"/>
    <text class="value" x="845" y="17" text-anchor="end">10.0mg</text>
  </g>
  <g class="row" transform="translate(0,630)">
    <rect class="label-box" x="8" y="0" width="148" height="45"/><text class="label-text" x="16" y="28">ビタミンB12</text>
    <rect class="bar-ours" x="156" y="9" width="330" height="8"/>
    <rect class="bar-mlm" x="156" y="29" width="114" height="8"/>
    <text class="value" x="512" y="42">10.0mcg</text>
  </g>
  <g class="row" transform="translate(0,679)">
    <rect class="label-box" x="8" y="0" width="148" height="45"/><text class="label-text" x="16" y="28">葉酸</text>
    <rect class="bar-ours" x="156" y="9" width="44" height="8"/>
    <rect class="bar-mlm" x="156" y="29" width="114" height="8"/>
    <text class="value" x="224" y="17">200mcg</text>
  </g>
  <g class="row" transform="translate(0,728)">
    <rect class="label-box" x="8" y="0" width="148" height="45"/><text class="label-text" x="16" y="28">ビオチン</text>
    <rect class="bar-ours" x="156" y="9" width="44" height="8"/>
    <rect class="bar-mlm" x="156" y="29" width="72" height="8"/>
    <text class="value" x="224" y="17">50mcg</text>
  </g>
  <g class="row" transform="translate(0,777)">
    <rect class="label-box" x="8" y="0" width="148" height="45"/><text class="label-text" x="16" y="28">カルシウム</text>
    <rect class="bar-ours" x="156" y="9" width="30" height="8"/>
    <rect class="bar-mlm" x="156" y="29" width="44" height="8"/>
    <text class="value" x="224" y="17">150mg</text>
  </g>
  <g class="row" transform="translate(0,826)">
    <rect class="label-box" x="8" y="0" width="148" height="45"/><text class="label-text" x="16" y="28">マグネシウム</text>
    <rect class="bar-ours" x="156" y="9" width="22" height="8"/>
    <rect class="bar-mlm" x="156" y="29" width="58" height="8"/>
    <text class="value" x="224" y="17">80mg</text>
  </g>
  <g class="row" transform="translate(0,875)">
    <rect class="label-box" x="8" y="0" width="148" height="45"/><text class="label-text" x="16" y="28">亜鉛</text>
    <rect class="bar-ours" x="156" y="9" width="38" height="8"/>
    <rect class="bar-mlm" x="156" y="29" width="72" height="8"/>
    <text class="value" x="224" y="17">5.0mg</text>
  </g>
  <g class="row" transform="translate(0,924)">
    <rect class="label-box" x="8" y="0" width="148" height="45"/><text class="label-text" x="16" y="28">マンガン</text>
    <rect class="bar-ours" x="156" y="9" width="30" height="8"/>
    <rect class="bar-mlm" x="156" y="29" width="66" height="8"/>
    <text class="value" x="224" y="17">1.0mg</text>
  </g>
  <g class="row" transform="translate(0,973)">
    <rect class="label-box" x="8" y="0" width="148" height="45"/><text class="label-text" x="16" y="28">クロム</text>
    <rect class="bar-ours" x="156" y="9" width="22" height="8"/>
    <rect class="bar-mlm" x="156" y="29" width="58" height="8"/>
    <text class="value" x="224" y="17">4mcg</text>
  </g>
  <g class="row" transform="translate(0,1022)">
    <rect class="label-box" x="8" y="0" width="148" height="45"/><text class="label-text" x="16" y="28">セレン</text>
    <rect class="bar-ours" x="156" y="9" width="22" height="8"/>
    <rect class="bar-mlm" x="156" y="29" width="66" height="8"/>
    <text class="value" x="224" y="17">10mcg</text>
  </g>
  <g class="row" transform="translate(0,1071)">
    <rect class="label-box" x="8" y="0" width="148" height="45"/><text class="label-text" x="16" y="28">銅</text>
    <rect class="bar-ours" x="156" y="9" width="100" height="8"/>
    <rect class="bar-mlm" x="156" y="29" width="72" height="8"/>
    <text class="value" x="268" y="17">1.0mg</text>
  </g>
  <g class="row" transform="translate(0,1120)">
    <rect class="label-box" x="8" y="0" width="148" height="45"/><text class="label-text" x="16" y="28">モリブデン</text>
    <rect class="bar-ours" x="156" y="9" width="22" height="8"/>
    <rect class="bar-mlm" x="156" y="29" width="66" height="8"/>
    <text class="value" x="224" y="17">4mcg</text>
  </g>

  <!-- scale breaks -->
  <g class="scale-break">
    <path class="break-gap" d="M780,336 q6,10 0,20 t0,20 t0,20 t0,20 t0,20 t0,20 t0,20 t0,20 t0,20 t0,20 t0,20 t0,20 t0,20 t0,20 t0,20"/>
    <path class="break-edge" d="M775,336 q6,10 0,20 t0,20 t0,20 t0,20 t0,20 t0,20 t0,20 t0,20 t0,20 t0,20 t0,20 t0,20 t0,20 t0,20 t0,20"/>
    <path class="break-edge" d="M785,336 q6,10 0,20 t0,20 t0,20 t0,20 t0,20 t0,20 t0,20 t0,20 t0,20 t0,20 t0,20 t0,20 t0,20 t0,20 t0,20"/>
    <path class="break-gap" d="M500,434 q6,10 0,20 t0,20 t0,20 t0,20 t0,20 t0,20 t0,20 t0,20 t0,20 t0,20 t0,20 t0,20"/>
    <path class="break-edge" d="M495,434 q6,10 0,20 t0,20 t0,20 t0,20 t0,20 t0,20 t0,20 t0,20 t0,20 t0,20 t0,20 t0,20"/>
    <path class="break-edge" d="M505,434 q6,10 0,20 t0,20 t0,20 t0,20 t0,20 t0,20 t0,20 t0,20 t0,20 t0,20 t0,20 t0,20"/>
  </g>

  <line class="baseline" x1="213" y1="106" x2="213" y2="1172"/>
</svg>
</div>
</body>
</html>
```